The Weave of Brightfold

We are running an international event in Switzerland on "Transmedia" with some of the hottest names in this hot media space ...

There will be 15 Keynote addresses and we are paying to have them professionally transcribed, copywritten, and proof-read to be published in an eBook.

The 15 Keynotes reference a huge number of global media brands - have a look: www.plimvoracast.com

We want a riveting, beautifully designed eBook cover and layout strategy - with the idea that this will be first of a series we will publish on different "Creative Industries" professional development issues - so MOST important is to think of the ARCHITECTURE of the artwork, as well as the graphic design ... think of the idea of an "imprint" in traditional book publishing - the architecture will remain the same, but the artwork and imagry will change each time.

Core values: Global media, Excellence, World's Best practitioners, Know How-to, Instant Inside Knowledge.

Target Market(s)

Professional Development for International Creative Industries Practitioners.

Industry/Entity Type

Graphic Design

Requirements
Must have
• Should be re-purposable across all other forms of media: it's "Transmedia", right? It should incorporate artwork, design, operate as a logo, typeface and font, and a basic imprint for a series of eBooks

The most important consideration in buying an Book is the Table of Content and the authors (we've got that in gold!) - The second-most important consideration is the artwork on the cover ... it has to be instantly convincing.

```html
<!DOCTYPE html>
<html lang="en">
<head>
<meta charset="utf-8">
<title>The Weave of Brightfold — Cover Spread</title>
<link rel="stylesheet" href="https://fonts.googleapis.com/css2?family=Jost:wght@400;500;700&display=swap">
<style>
  :root {
    --canvas-bg: #e8e8e8;
    --cover-black: #0b0b0b;
    --cover-charcoal: #1c1c1c;
    --title-white: #f2f2f2;
    --back-title: #cfcfcf;
    --body-grey: #b9b9b9;
    --spine-grey: #cfcfcf;
    --spine-author: #8a8a8a;
    --box-grey: #2f2f2f;
    --box-text: #9a9a9a;
    --photo-dark: #141414;
    --photo-mid: #3c3c3c;
    --photo-light: #6a6a6a;
    --photo-glow: rgba(225,225,225,0.55);
    --photo-accent: rgba(190,20,24,0.55);
  }
  * { box-sizing: border-box; margin: 0; padding: 0; }
  html, body { width: 1200px; height: 800px; overflow: hidden; }
  body {
    background: var(--canvas-bg);
    font-family: "Jost", "Century Gothic", sans-serif;
  }
  .spread {
    position: absolute;
    left: 178px; top: 110px;
    width: 844px; height: 580px;
    display: flex;
    box-shadow: 0 14px 40px rgba(0,0,0,0.25);
  }
  .back-cover, .front-cover, .spine {
    height: 100%;
    background: var(--cover-black);
    position: relative;
  }
  .back-cover { width: 400px; padding: 22px 34px 0; }
  .spine {
    width: 44px;
    background: linear-gradient(90deg, #000 0%, var(--cover-charcoal) 50%, #000 100%);
    display: flex; flex-direction: column; align-items: center;
    justify-content: space-between;
    padding: 14px 0 16px;
  }
  .front-cover { width: 400px; overflow: hidden; }

  .author-name {
    font-size: 11px; font-weight: 500;
    color: var(--title-white);
    text-align: right;
  }
  .book-title {
    font-weight: 700;
    color: var(--title-white);
    text-transform: uppercase;
    line-height: 1.08;
    text-align: center;
    letter-spacing: 0.5px;
  }
  .back-cover .book-title { font-size: 36px; margin-top: 2px; color: var(--back-title); }
  .back-cover .author-name { padding-right: 20px; color: var(--back-title); }

  .blurb {
    margin-top: 14px;
    font-size: 11.2px; line-height: 1.5;
    color: var(--body-grey);
    text-align: justify;
    text-align-last: center;
  }
  .back-marks {
    position: absolute; left: 34px; right: 34px; bottom: 22px;
    display: flex; justify-content: space-between;
  }
  .placeholder-box {
    width: 82px; height: 44px;
    background: var(--box-grey);
    color: var(--box-text);
    font-size: 11px;
    display: flex; align-items: center; justify-content: center;
  }

  .spine-title, .spine-author {
    writing-mode: vertical-rl;
    color: var(--spine-grey);
    text-transform: uppercase;
  }
  .spine-title { font-size: 26px; font-weight: 700; letter-spacing: 1px; }
  .spine-author { font-size: 9px; text-transform: none; color: var(--spine-author); }

  .front-cover .author-name { position: absolute; top: 36px; right: 48px; z-index: 2; }
  .front-cover .book-title {
    position: absolute; top: 54px; left: 0; right: 0;
    font-size: 46px; z-index: 2;
  }
  .cover-photo {
    position: absolute; left: 0; right: 0; top: 150px; bottom: 0;
    background:
      radial-gradient(ellipse 14% 9% at 50% 22%, var(--photo-glow), transparent 100%),
      radial-gradient(ellipse 22% 14% at 64% 74%, var(--photo-accent), transparent 100%),
      radial-gradient(ellipse 70% 48% at 52% 62%, var(--photo-light), transparent 100%),
      linear-gradient(180deg, var(--cover-black) 0%, var(--photo-dark) 18%, var(--photo-mid) 55%, #2e2e2e 82%, var(--photo-dark) 100%);
  }
</style>
</head>
<body>
  <main class="spread">
    <section class="back-cover">
      <p class="author-name">Author's Name</p>
      <h2 class="book-title">The Weave of<br>Brightfold</h2>
      <p class="blurb">Lorem ipsum dolor sit amet, consectetur adipisicing elit, sed do eiusmod tempor incididunt ut labore et dolore magna aliqua. Ut enim ad minim veniam, quis nostrud exercitation. Lorem ipsum dolor sit amet, consectetur adipisicing elit, sed do eiusmod tempor incididunt ut labore et dolore magna aliqua. Ut enim ad minim veniam, quis nostrud exercitation. Lorem ipsum dolor sit amet, consectetur adipisicing elit, sed do eiusmod tempor incididunt ut labore et dolore magna aliqua. Ut enim ad minim veniam, quis nostrud exercitation. Lorem ipsum dolor sit amet, consectetur adipisicing elit, sed do eiusmod tempor incididunt ut labore et dolore magna aliqua. Ut enim ad minim veniam, quis nostrud exercitation. Lorem ipsum dolor sit amet, consectetur adipisicing elit, sed do eiusmod tempor incididunt ut labore et dolore magna aliqua. Ut enim ad minim veniam, quis nostrud exercitation. Lorem ipsum dolor sit amet, consectetur adipisicing elit, sed do eiusmod tempor incididunt ut labore et dolore magna aliqua. Ut enim ad minim veniam, quis nostrud exercitation. Lorem ipsum dolor sit amet, consectetur adipisicing elit, sed do eiusmod tempor incididunt ut labore et dolore magna aliqua. Ut enim ad minim veniam, quis nostrud exercitation.</p>
      <div class="back-marks">
        <div class="placeholder-box">LOGO</div>
        <div class="placeholder-box">ISBN</div>
      </div>
    </section>

    <section class="spine">
      <span class="spine-title">The Weave of Brightfold</span>
      <span class="spine-author">Author's Name</span>
    </section>

    <section class="front-cover">
      <div class="cover-photo" role="img" aria-label="Photograph of a businessman in a grey suit holding an open red laptop, beneath a glowing light bulb, set against a dark digital backdrop of binary code and bar graphs"></div>
      <p class="author-name">Author's Name</p>
      <h1 class="book-title">The Weave of<br>Brightfold</h1>
    </section>
  </main>
</body>
</html>
```